New Business Card Design Project

Updated business card design. I am moving towards more coaching of, for the most part women, who are searching for more in their lives. I am an intuitive healer, homeopath and nutritionist but also an author and motivational speaker. Int the past I have included my photo on the card but that is not essential. My book is called the Brilliance of Saffron - Reclaiming the Shade of Your Spirit so my colours are typically magenta.
Target Market(s)
Women - 35 - 60 considering improving their health. However, I am also a professional speaker with a target audience including corporate and conferences.
Industry/Entity Type
Health And Wellness
Contact Information for Business Card
Lucinda Parvell, Hom, RHN, BA
www.lucindaparvell.com
lucinda@lucindaparvell.com
519-362-7015
Facebook, instagram and twitter logos
Look and feel
Each slider illustrates characteristics of the customer's brand and the style your logo design should communicate.

```html
<!DOCTYPE html>
<html lang="en">
<head>
<meta charset="utf-8">
<title>Lucinda Parvell – Business Card</title>
<link href="https://fonts.googleapis.com/css2?family=Noto+Serif:wght@400;500&display=swap" rel="stylesheet">
<style>
  :root {
    --bg: #dedede;
    --card-white: #f6f6f4;
    --magenta: #d8317f;
    --magenta-deep: #c92672;
    --magenta-light: #e67aab;
    --ink: #1d1a1c;
    --text-light: #fbe9f1;
    --icon-dot: #8e3f8a;
  }
  html, body {
    margin: 0;
    width: 1200px;
    height: 975px;
    overflow: hidden;
    background: var(--bg);
  }
  .card {
    position: absolute;
    left: 100px;
    top: 202px;
    width: 1000px;
    height: 571px;
    background: var(--card-white);
    box-shadow: 0 18px 40px rgba(0,0,0,0.18);
    overflow: hidden;
  }
  .card-bands {
    position: absolute;
    inset: 0;
  }
  .brand {
    position: absolute;
    left: 0;
    right: 0;
    top: 78px;
    display: flex;
    justify-content: center;
    align-items: center;
    gap: 20px;
  }
  .brand-dot {
    width: 48px;
    height: 48px;
    border-radius: 50%;
    background: var(--magenta);
    flex: none;
  }
  .brand-name {
    font-family: "Noto Serif", serif;
    font-weight: 400;
    font-size: 72px;
    color: var(--ink);
    line-height: 1;
  }
  .contact {
    position: absolute;
    left: 360px;
    top: 335px;
    font-family: "Noto Serif", serif;
    color: var(--text-light);
  }
  .contact-name {
    font-size: 30px;
    font-weight: 500;
    margin: 0 0 8px;
  }
  .credentials {
    font-size: 19px;
    margin-left: 14px;
  }
  .contact-line {
    display: flex;
    align-items: center;
    gap: 14px;
    font-size: 27px;
    margin: 6px 0;
  }
  .contact-icon {
    width: 22px;
    height: 22px;
    flex: none;
  }
  .social {
    position: absolute;
    left: 760px;
    top: 478px;
    display: flex;
    gap: 14px;
  }
  .social-dot {
    width: 24px;
    height: 24px;
    border-radius: 50%;
    background: var(--icon-dot);
  }
</style>
</head>
<body>
  <div class="card">
    <svg class="card-bands" viewBox="0 0 1000 571" width="1000" height="571" aria-hidden="true">
      <path d="M0,300 C300,200 700,175 1000,185 L1000,571 L0,571 Z" fill="var(--magenta-light)"/>
      <path d="M0,330 C330,245 700,230 1000,300 L1000,571 L0,571 Z" fill="var(--magenta)"/>
    </svg>
    <svg class="card-bands" viewBox="0 0 1000 571" width="1000" height="571" role="img" aria-label="Decorative swirl-patterned head silhouette">
      <defs>
        <clipPath id="band-clip">
          <path d="M0,330 C330,245 700,230 1000,300 L1000,571 L0,571 Z"/>
        </clipPath>
      </defs>
      <circle cx="110" cy="450" r="160" fill="var(--magenta-deep)" clip-path="url(#band-clip)"/>
    </svg>

    <div class="brand">
      <span class="brand-dot"></span>
      <span class="brand-name">Lucinda Parvell</span>
    </div>

    <div class="contact">
      <p class="contact-name">Lucinda Parvell <span class="credentials">Hom, RHN, BA</span></p>
      <div class="contact-line">
        <svg class="contact-icon" viewBox="0 0 24 24" fill="none" stroke="currentColor" stroke-width="2"><circle cx="12" cy="12" r="10"/><path d="M2 12h20M12 2c3 3 3 17 0 20M12 2c-3 3-3 17 0 20"/></svg>
        www.lucindaparvell.com
      </div>
      <div class="contact-line">
        <svg class="contact-icon" viewBox="0 0 24 24" fill="none" stroke="currentColor" stroke-width="2"><rect x="2" y="5" width="20" height="14"/><path d="M2 5l10 8 10-8"/></svg>
        lucinda@lucindaparvell.com
      </div>
      <div class="contact-line">
        <svg class="contact-icon" viewBox="0 0 24 24" fill="currentColor"><path d="M6.6 10.8a15 15 0 0 0 6.6 6.6l2.2-2.2a1 1 0 0 1 1-.25 11 11 0 0 0 3.6.6 1 1 0 0 1 1 1V20a1 1 0 0 1-1 1A17 17 0 0 1 3 4a1 1 0 0 1 1-1h3.5a1 1 0 0 1 1 1 11 11 0 0 0 .6 3.6 1 1 0 0 1-.25 1Z"/></svg>
        519-362-7015
      </div>
    </div>

    <div class="social" aria-label="Social media">
      <span class="social-dot"></span>
      <span class="social-dot"></span>
      <span class="social-dot"></span>
    </div>
  </div>
</body>
</html>
```